Craft brewery website - Harrow Lane Brewery

Looking for a simple site similar to fennimoorales.com or tallwharf.com with the following features:
- incorporates existing logo (file attached)
- has a consistent look and feel throughout the site that works in harmony with the logo. Please suggest a cool font to use!
- incorporates all or some of the attached images
- has the following tabs/pages: home, our story, brews, blog, contact.
- has some sort of prominent image/design under the top menu bar that can be updated with content - so a placeholder for text. Please use this text on home page: "we brew up our passion for honest ingredients, our curiosity for different cultures, and social and environmental consciousness into characteristic beers." And "Beers with a Twist for the good of the world, for the fun of the party"
- has a scrolling set of images under main section that will list beers. Please create five placeholders for beers: Weizenbock, Wandering Heron, Stout, Saison, Dusty Hal

Industry/Entity Type

Brewery

Number of Pages Required

1 page

Requirements
Must have
• Looking for a simple site similar to fennimoorales.com with the following features:
• - incorporates existing logo (file attached)
• - has a consistent look and feel throughout the site that works in harmony with the logo. Please suggest a cool font to use!
• - incorporates all or some of the attached images
• - has the following tabs/pages: home, our story, brews, blog, contact.
• - has some sort of prominent image/design under the top menu bar that can be updated with content - so a placeholder for text. Please use this text on home page: "we brew up our passion for honest ingredients, our curiosity for different cultures, and social and environmental consciousness into characteristic beers." And "Beers with a Twist for the good of the world, for the fun of the party"
• - has a scrolling set of images under main section that will list beers. Please create five placeholders for beers: Weizenbock, Wandering Heron, Stout, Saison, Dusty Hal

```html
<!DOCTYPE html>
<html lang="en">
<head>
<meta charset="utf-8">
<title>Harrow Lane Brewery</title>
<link rel="stylesheet" href="https://fonts.googleapis.com/css2?family=Jost:wght@400;500;700;800&display=swap">
<style>
:root{
  --gold:#b38a2e;
  --navy:#141c52;
  --ink:#2a2a2a;
  --muted:#555;
  --rule:#d6d6d6;
  --white:#fff;
}
*{box-sizing:border-box;margin:0;padding:0}
html,body{width:946px;height:1200px;overflow:hidden;background:var(--white)}
body{font-family:"Jost",sans-serif;color:var(--ink);position:relative}
.site-nav{position:absolute;top:0;left:0;width:946px;height:70px;background:var(--white)}
.nav-link{position:absolute;top:29px;font-size:14.5px;font-weight:500;letter-spacing:.3px;color:var(--ink);text-decoration:none;text-transform:uppercase}
.nav-link.is-active{color:var(--gold)}
.nav-search{position:absolute;left:819px;top:31px}
.brand-badge{position:absolute;left:403px;top:8px;width:140px;height:140px;border-radius:50%;background:var(--white);border:3px solid var(--gold);display:flex;align-items:center;justify-content:center;text-align:center;z-index:3}
.brand-name{font-weight:700;font-size:17px;line-height:1.15;color:var(--navy);text-transform:uppercase;letter-spacing:1px}
.hero{position:absolute;top:70px;left:0;width:946px;height:400px;background:linear-gradient(100deg,#cfc9bf 0%,#c9c3b8 45%,#bdb6ab 70%,#c7c1b6 100%);overflow:hidden}
.hero-art{position:absolute;inset:0}
.hero-title{position:absolute;top:160px;width:100%;text-align:center;font-size:50px;font-weight:800;letter-spacing:2px;color:var(--white);text-shadow:0 2px 6px rgba(0,0,0,.35);text-transform:uppercase}
.hero-dots{position:absolute;top:339px;left:439px;display:flex;gap:4px}
.hero-dot{width:14px;height:14px;border-radius:50%;border:1.5px solid var(--white)}
.hero-dot.is-current{background:var(--white)}
.intro{position:absolute;top:506px;left:130px;width:686px;text-align:center;font-size:16px;line-height:28px;font-weight:500;color:var(--ink)}
.beer-list{position:absolute;top:625px;left:38px;width:870px;display:flex;justify-content:space-between}
.beer{width:160px;text-align:center}
.beer-shot{display:block;width:120px;height:188px;margin:0 auto;border-radius:6px}
.beer-name{margin-top:16px;font-size:18px;font-weight:500;color:var(--ink)}
.btn-beers{position:absolute;left:386px;top:894px;width:175px;height:37px;border:1px solid #888;display:flex;align-items:center;justify-content:center;font-size:14.5px;font-weight:500;color:var(--gold);text-transform:uppercase;letter-spacing:.3px;text-decoration:none}
.footer-band{position:absolute;top:993px;left:0;width:946px;height:3px;background:var(--navy)}
.footer-contact{position:absolute;top:1032px;left:0;width:946px;display:flex;justify-content:center;gap:30px;font-size:13px;color:var(--ink)}
.contact-item{display:flex;align-items:center;gap:10px}
.contact-icon{width:28px;height:28px;border-radius:50%;border:1.5px solid var(--gold);display:flex;align-items:center;justify-content:center}
.footer-links{position:absolute;top:1083px;left:0;width:946px;text-align:center;font-size:12.5px;color:var(--ink)}
.footer-links a{color:var(--ink);text-decoration:none}
.footer-links .sep{margin:0 16px}
.footer-rule{position:absolute;top:1132px;left:75px;width:791px;height:1px;background:var(--rule)}
.copyright{position:absolute;top:1161px;left:74px;font-size:10px;color:var(--muted)}
.social{position:absolute;top:1154px;left:688px;display:flex;gap:9px}
.social-dot{width:29px;height:29px;border-radius:50%;border:1.5px solid var(--gold)}
</style>
</head>
<body>
<header class="site-nav">
  <a class="nav-link is-active" style="left:108px" href="#">Home</a>
  <a class="nav-link" style="left:199px" href="#">Our Story</a>
  <a class="nav-link" style="left:322px" href="#">Brews</a>
  <a class="nav-link" style="left:584px" href="#">Blog</a>
  <a class="nav-link" style="left:689px" href="#">Contact</a>
  <svg class="nav-search" width="16" height="16" viewBox="0 0 16 16" aria-label="Search"><circle cx="6.5" cy="6.5" r="5" fill="none" stroke="#2a2a2a" stroke-width="2"/><line x1="10" y1="10" x2="14.5" y2="14.5" stroke="#2a2a2a" stroke-width="2.4" stroke-linecap="round"/></svg>
</header>

<div class="brand-badge"><span class="brand-name">Harrow Lane<br>Brewery</span></div>

<section class="hero">
  <div class="hero-art" role="img" aria-label="Photo of a painted street mural on a weathered wall in grey, red, blue and black tones"></div>
  <h1 class="hero-title">Harrow Lane Brewery</h1>
  <div class="hero-dots"><span class="hero-dot is-current"></span><span class="hero-dot"></span><span class="hero-dot"></span><span class="hero-dot"></span></div>
</section>

<p class="intro">We brew up our passion for honest ingredients, our curiosity for different cultures, and social and environmental consciousness into characteristic beers." And "Beers with a Twist for the good of the world, for the fun of the party"</p>

<ul class="beer-list" style="list-style:none">
  <li class="beer"><span class="beer-shot" role="img" aria-label="Weizenbock bottle and glass" style="background:linear-gradient(180deg,#f1ece6 0%,#6e2230 35%,#4a1a3c 100%)"></span><p class="beer-name">Weizenbock</p></li>
  <li class="beer"><span class="beer-shot" role="img" aria-label="Wandering Heron bottle and glass" style="background:linear-gradient(180deg,#f3efe8 0%,#b0561e 35%,#5a2a10 100%)"></span><p class="beer-name">Wandering Heron</p></li>
  <li class="beer"><span class="beer-shot" role="img" aria-label="Stout bottle and glass" style="background:linear-gradient(180deg,#e4d6c0 0%,#2a1a14 30%,#141010 100%)"></span><p class="beer-name">Stout</p></li>
  <li class="beer"><span class="beer-shot" role="img" aria-label="Saison bottle and glass" style="background:linear-gradient(180deg,#faf6ee 0%,#f1c23a 40%,#d8641e 100%)"></span><p class="beer-name">Saison</p></li>
  <li class="beer"><span class="beer-shot" role="img" aria-label="Dusty Hal bottle and glass" style="background:linear-gradient(180deg,#f3ece0 0%,#d9a33c 40%,#7a2416 100%)"></span><p class="beer-name">Dusty Hal</p></li>
</ul>

<a class="btn-beers" href="#">Meet the Beers</a>

<div class="footer-band"></div>
<footer>
  <div class="footer-contact">
    <span class="contact-item"><span class="contact-icon"><svg width="14" height="11" viewBox="0 0 14 11"><rect x="1" y="1" width="12" height="9" rx="1" fill="none" stroke="#b38a2e" stroke-width="1.3"/><polyline points="1,1.5 7,6 13,1.5" fill="none" stroke="#b38a2e" stroke-width="1.3"/></svg></span>info@harrowlanebrewery.com.au</span>
    <span class="contact-item"><span class="contact-icon"><svg width="13" height="13" viewBox="0 0 24 24"><path d="M6.6 10.8a15 15 0 0 0 6.6 6.6l2.2-2.2a1 1 0 0 1 1-.25 11.4 11.4 0 0 0 3.6.57 1 1 0 0 1 1 1V20a1 1 0 0 1-1 1A17 17 0 0 1 3 4a1 1 0 0 1 1-1h3.5a1 1 0 0 1 1 1c0 1.25.2 2.45.57 3.57a1 1 0 0 1-.25 1z" fill="#b38a2e"/></svg></span>1 800 555 0142</span>
  </div>
  <nav class="footer-links"><a href="#">Home</a><span class="sep">|</span><a href="#">Our story</a><span class="sep">|</span><a href="#">Brews</a><span class="sep">|</span><a href="#">Blog</a><span class="sep">|</span><a href="#">Contact</a></nav>
  <div class="footer-rule"></div>
  <p class="copyright">Copyright © 2017, Harrow Lane Brewery. All Right Reserved</p>
  <div class="social"><span class="social-dot"></span><span class="social-dot"></span><span class="social-dot"></span><span class="social-dot"></span><span class="social-dot"></span></div>
</footer>
</body>
</html>
```